The name of the company is Dorvane Holdings, LLC. I would like a business card with a logo.

On the top left, I would like a logo design of a crown and I would like Dorvane over the top of the crown while Investments on the bottom. Please see attached files as an example of crown and positioning of Dorvane Holdings. Then I would like the letters DH in the middle(see picture).

Colors

Designer to choose colors to be used in the design.

```html
<!DOCTYPE html>
<html lang="en">
<head>
<meta charset="utf-8">
<title>Dorvane Holdings, LLC — Business Card</title>
<link href="https://fonts.googleapis.com/css2?family=Roboto:wght@400;500;700&display=swap" rel="stylesheet">
<style>
  :root {
    --page-bg: #2b2b2d;
    --card-bg: #1c1c1d;
    --card-edge: #111112;
    --gold: #f4b921;
    --white: #f2f2f2;
  }
  * { box-sizing: border-box; margin: 0; padding: 0; }
  html, body {
    width: 1200px; height: 960px; overflow: hidden;
    background: var(--page-bg);
    font-family: "Roboto", Arial, sans-serif;
  }
  .stage {
    width: 1200px; height: 960px;
    display: flex; flex-direction: column; align-items: center;
    justify-content: center; gap: 50px;
  }
  .card {
    position: relative; width: 700px; height: 400px;
    background: var(--card-bg);
    border-radius: 22px;
    box-shadow: 0 4px 0 var(--card-edge), 0 14px 28px rgba(0,0,0,.45);
  }

  /* Brand lockup: plain circle with the company name stacked beside it */
  .brand { display: flex; align-items: center; }
  .brand-dot { flex: none; border-radius: 50%; background: var(--gold); }
  .brand-name { color: var(--gold); font-weight: 500; line-height: 1.08; }

  /* Front */
  .card-front { display: flex; align-items: center; justify-content: center; }
  .card-front .brand { gap: 30px; }
  .card-front .brand-dot { width: 150px; height: 150px; }
  .card-front .brand-name { font-size: 54px; }

  /* Back */
  .card-back .brand { position: absolute; left: 44px; top: 38px; gap: 20px; }
  .card-back .brand-dot { width: 96px; height: 96px; }
  .card-back .brand-name { font-size: 32px; }

  .person { position: absolute; right: 44px; top: 40px; text-align: right; }
  .person-name { color: var(--gold); font-weight: 700; font-size: 30px; }
  .person-role { color: var(--white); font-size: 20px; margin-top: 2px; }

  .contact {
    position: absolute; left: 44px; bottom: 34px;
    color: var(--white); font-size: 22px; line-height: 1.32;
  }
  .contact-company { color: var(--gold); font-weight: 500; }
  .contact-row { display: flex; align-items: center; gap: 12px; }
  .contact-row svg { width: 18px; height: 18px; flex: none; }
</style>
</head>
<body>
<main class="stage">
  <section class="card card-front" aria-label="Card front">
    <div class="brand">
      <span class="brand-dot"></span>
      <span class="brand-name">Dorvane<br>Holdings, LLC</span>
    </div>
  </section>

  <section class="card card-back" aria-label="Card back">
    <div class="brand">
      <span class="brand-dot"></span>
      <span class="brand-name">Dorvane<br>Holdings, LLC</span>
    </div>

    <div class="person">
      <div class="person-name">Navid Dorvane</div>
      <div class="person-role">Founder/CEO</div>
    </div>

    <div class="contact">
      <div class="contact-company">Dorvane Holdings, LLC</div>
      <div>418 Brennet Ridge Road, suite 200</div>
      <div>Harlow Hills Estates CA, 90431</div>
      <div class="contact-row">
        <svg viewBox="0 0 24 24" aria-hidden="true"><path fill="#f4b921" d="M6.6 10.8a15.2 15.2 0 0 0 6.6 6.6l2.2-2.2c.3-.3.7-.4 1-.2 1.1.4 2.3.6 3.6.6.6 0 1 .4 1 1V20c0 .6-.4 1-1 1A17 17 0 0 1 3 4c0-.6.4-1 1-1h3.5c.6 0 1 .4 1 1 0 1.3.2 2.5.6 3.6.1.3 0 .7-.2 1z"/></svg>
        <span>(555) 014-2290</span>
      </div>
      <div class="contact-row">
        <svg viewBox="0 0 24 24" aria-hidden="true"><rect x="2" y="5" width="20" height="14" rx="1.5" fill="#f4b921"/><path d="M3 6l9 7 9-7" fill="none" stroke="#1c1c1d" stroke-width="1.6"/></svg>
        <span>dorvane.holdings@mailbox.com</span>
      </div>
    </div>
  </section>
</main>
</body>
</html>
```